Harborline Stay Collective Business Card Design

Design a business card for Harborline Stay Collective. Look at the website for colors and reference. Card should have logo, name, title, office number, mobile number, email, URL and a tagline like, "Luxury Hotel & Resort Email Marketing" (This might change).

https://www.harborlinestaycollective.net

The rest I will leave up to your imagination.

Contact Information for Business Card

Logo, name, title, office number, mobile number, email, URL and a tagline like, "Luxury Hotel & Resort Email Marketing" (This might change).

```html
<!DOCTYPE html>
<html lang="en">
<head>
<meta charset="utf-8">
<title>Harborline Stay Collective — Business Card</title>
<link href="https://fonts.googleapis.com/css2?family=Josefin+Sans:wght@400;600;700&display=swap" rel="stylesheet">
<style>
  :root {
    --orange: #e8711f;
    --black: #060606;
    --white: #ffffff;
    --paper: #f3f3f3;
    --ink: #151515;
    --stage: #2b2b2b;
  }
  * { box-sizing: border-box; margin: 0; padding: 0; }
  html, body { width: 1200px; height: 900px; overflow: hidden; }
  body {
    background: var(--stage);
    font-family: "Josefin Sans", sans-serif;
    position: relative;
  }
  .card {
    position: absolute;
    left: 300px;
    width: 600px;
    height: 343px;
    background: var(--orange);
    box-shadow: 0 12px 30px rgba(0,0,0,0.45);
  }
  .card--front { top: 70px; }
  .card--back { top: 480px; }
  .card__panel {
    position: absolute;
    inset: 16px;
    clip-path: polygon(
      0 0, 100% 0,
      100% 76%, calc(100% - 16px) 76%, calc(100% - 16px) 100%,
      38% 100%, 38% calc(100% - 14px), 0 calc(100% - 14px)
    );
    display: flex;
    flex-direction: column;
    align-items: center;
    justify-content: center;
    text-align: center;
  }
  .card--front .card__panel { background: var(--black); color: var(--white); }
  .card--back .card__panel {
    background: linear-gradient(110deg, #dedede 0%, var(--white) 45%, var(--paper) 100%);
    color: var(--ink);
  }
  .brand {
    display: flex;
    align-items: center;
    gap: 10px;
    font-weight: 700;
    text-transform: uppercase;
    letter-spacing: 1px;
    line-height: 1;
  }
  .brand__mark {
    width: 14px; height: 14px;
    background: var(--orange);
  }
  .card--front .brand { font-size: 27px; margin-bottom: 14px; }
  .card--back .brand { font-size: 25px; margin-bottom: 16px; }
  .tagline { font-weight: 600; font-size: 17px; letter-spacing: 0.3px; }
  .card--back .tagline { margin-top: 14px; font-size: 16px; font-weight: 700; }
  .person__name {
    color: var(--orange);
    font-weight: 700;
    font-size: 17px;
    text-transform: uppercase;
    letter-spacing: 0.5px;
  }
  .person__title { font-size: 13px; margin-top: 2px; margin-bottom: 10px; }
  .contact { list-style: none; font-size: 12.5px; line-height: 1.6; }
  .contact li { display: flex; align-items: center; justify-content: center; gap: 6px; }
  .contact svg { width: 12px; height: 12px; fill: none; stroke: var(--orange); stroke-width: 2; }
  .contact .sep { margin: 0 4px; }
</style>
</head>
<body>
  <section class="card card--front" aria-label="Card front">
    <div class="card__panel">
      <div class="brand"><span class="brand__mark"></span>Harborline Stay Collective</div>
      <p class="tagline">Luxury Hotel &amp; Resort Email Marketing</p>
    </div>
  </section>

  <section class="card card--back" aria-label="Card back">
    <div class="card__panel">
      <div class="brand"><span class="brand__mark"></span>Harborline Stay Collective</div>
      <p class="person__name">Daniel Reeve</p>
      <p class="person__title">Director</p>
      <ul class="contact">
        <li>
          <svg viewBox="0 0 12 12"><rect x="3" y="1" width="6" height="10" rx="1"/></svg>555.010.0000
          <span class="sep">|</span>
          <svg viewBox="0 0 12 12"><path d="M2 2 L4.5 2 L5.5 4.5 L4 5.5 Q5 7.5 6.5 8 L7.5 6.5 L10 7.5 L10 10 Q4 10 2 2 Z"/></svg>555.014.2200
        </li>
        <li>
          <svg viewBox="0 0 12 12"><path d="M6 11 Q2 6.5 2 4.5 A4 4 0 0 1 10 4.5 Q10 6.5 6 11 Z"/><circle cx="6" cy="4.5" r="1.3"/></svg>North America
        </li>
        <li>
          <svg viewBox="0 0 12 12"><rect x="1" y="2.5" width="10" height="7"/><path d="M1 2.5 L6 6.5 L11 2.5"/></svg>info@harborlinestaycollective.net
        </li>
        <li>
          <svg viewBox="0 0 12 12"><circle cx="6" cy="6" r="5"/><path d="M1 6 H11 M6 1 Q3 6 6 11 M6 1 Q9 6 6 11"/></svg>www.harborlinestaycollective.net
        </li>
      </ul>
      <p class="tagline">Luxury Hotel &amp; Resort Email Marketing</p>
    </div>
  </section>
</body>
</html>
```